An e-flyer for an exotic car and fine wine club.

This is the first meeting of Birchwell Motor Society and includes several businesses. Their logos should be featured at the bottom. It should be sleek, elegant and simple featuring a photo of an Corvane Lestrel R7 as well as my logo (I will provide photos). The flyer needs to look professional and appeal to billionaires.
The text should read:
Birchwell Motor society presents
Fast Cars and Fine Wine (but not while driving)
Hosted by Harlow Gem Vault
Bring your best car(s) and join us to enjoy the party with sommelier selected wines, the best classic and modern cars and hors d'oeuvre catered by Penrose's Clam House. Live DJ.
August 26th 3-6 p.m.
This event is gratis.
RSVP to dana@birchwellmotors.example for address and details

Target Market(s)
Very wealthy exotic car owners
Industry/Entity Type
Car Club, Fine Wines.
Requirements
Must have
- Style, panache, elegance, sleekness, simplicity. I like the idea of a black or dark flyer with a consistent color scheme.
Nice to have
- I want the flyer to be simple and sleek, feature an Corvane Lestrel R7 as the eye catcher, Birchwell Motor Society logo featured prominently on the top, and the other business logos on the bottom.
Should not have
- It must not be too noisy or busy.

```html
<!DOCTYPE html>
<html lang="en">
<head>
<meta charset="utf-8">
<title>Fast Cars &amp; Fine Wine — Birchwell Motor Society</title>
<link rel="stylesheet" href="https://fonts.googleapis.com/css2?family=Arimo:wght@400;700&family=Bungee&family=Oswald:wght@500&family=Montserrat:wght@500;700&display=swap">
<style>
  :root {
    --frame: #dcdedd;
    --paper: #ffffff;
    --crimson: #c4293f;
    --crimson-light: #e2364a;
    --ink: #333333;
    --body-ink: #484848;
    --partner-orange: #f26522;
    --car-top: #d23a48;
    --car-mid: #b42334;
    --car-low: #5a1119;
  }
  * { margin: 0; padding: 0; box-sizing: border-box; }
  html, body { width: 849px; height: 1200px; overflow: hidden; background: var(--frame); }
  .flyer { position: relative; width: 849px; height: 1200px; background: var(--frame); font-family: "Arimo", sans-serif; }
  .sheet { position: absolute; left: 50px; top: 42px; width: 748px; height: 1116px; background: var(--paper); }
  .abs { position: absolute; }

  .club-name {
    left: 238px; top: 96px; width: 373px; text-align: center;
    font-family: "Montserrat", sans-serif; font-weight: 700; color: var(--ink);
    font-size: 25px; letter-spacing: 7px; line-height: 40px; text-transform: uppercase;
  }
  .presents {
    left: 238px; top: 204px; width: 373px; text-align: center;
    font-family: "Montserrat", sans-serif; font-weight: 700; font-size: 11px;
    letter-spacing: 12.5px; color: var(--crimson); padding-left: 12px;
  }

  .title-panel { left: 238px; top: 227px; width: 373px; height: 400px; background: var(--crimson); }
  .headline { left: 238px; top: 227px; }

  .tagline {
    left: 238px; top: 520px; width: 373px; text-align: center;
    font-weight: 700; font-size: 11px; color: var(--paper); letter-spacing: 0.2px;
  }
  .host {
    left: 238px; top: 539px; width: 373px; text-align: center;
    font-weight: 700; font-size: 16.5px; color: var(--paper);
  }

  .car-photo {
    left: 128px; top: 567px; width: 594px; height: 175px;
    background: linear-gradient(180deg, var(--car-top) 0%, var(--car-mid) 55%, var(--car-low) 100%);
  }

  .details {
    left: 247px; top: 758px; width: 354px;
    font-size: 13.4px; line-height: 21px; color: var(--body-ink); text-align: justify; text-align-last: justify;
  }
  .live-dj {
    left: 238px; top: 824px; width: 373px; text-align: center;
    font-weight: 700; font-size: 25px; color: var(--crimson);
  }
  .date-band {
    left: 238px; top: 866px; width: 373px; height: 58px; background: var(--crimson);
    display: flex; align-items: center; justify-content: center;
    font-family: "Oswald", sans-serif; font-weight: 500; font-size: 42px; color: var(--paper);
    letter-spacing: 0; line-height: 1;
  }
  .date-band sup { font-size: 19px; position: relative; top: -8px; margin-right: 12px; }

  .rsvp {
    left: 238px; top: 939px; width: 373px; text-align: center;
    font-size: 13.4px; line-height: 21px; color: var(--ink);
  }
  .rsvp .email { color: var(--crimson); }

  .partners { left: 238px; top: 1014px; }
  .partner-name {
    top: 1062px; width: 186px; text-align: center;
    font-family: "Montserrat", sans-serif; font-weight: 700; font-size: 15px;
    letter-spacing: 0.5px; text-transform: uppercase; white-space: nowrap;
  }
  .partner-vault { left: 238px; color: var(--partner-orange); }
  .partner-cellars { left: 425px; color: var(--ink); }
</style>
</head>
<body>
<main class="flyer">
  <div class="sheet"></div>

  <header>
    <p class="abs club-name">Birchwell<br>Motor Society</p>
    <p class="abs presents">PRESENTS</p>
  </header>

  <section class="title-block">
    <div class="abs title-panel"></div>
    <svg class="abs headline" width="373" height="300" viewBox="0 0 373 300" aria-label="Fast Cars and Fine Wine">
      <g stroke="#ffffff" stroke-width="1">
        <line x1="52" y1="46" x2="128" y2="46"/><line x1="52" y1="49.5" x2="128" y2="49.5"/><line x1="52" y1="53" x2="128" y2="53"/>
        <line x1="245" y1="46" x2="321" y2="46"/><line x1="245" y1="49.5" x2="321" y2="49.5"/><line x1="245" y1="53" x2="321" y2="53"/>
        <line x1="52" y1="185" x2="128" y2="185"/><line x1="52" y1="188.5" x2="128" y2="188.5"/><line x1="52" y1="192" x2="128" y2="192"/>
        <line x1="245" y1="185" x2="321" y2="185"/><line x1="245" y1="188.5" x2="321" y2="188.5"/><line x1="245" y1="192" x2="321" y2="192"/>
      </g>
      <text x="186.5" y="58" text-anchor="middle" fill="#ffffff" font-family="Montserrat, sans-serif" font-weight="700" font-size="23" letter-spacing="6">FAST</text>
      <text x="44" y="148" fill="#ffffff" font-family="Bungee, sans-serif" font-size="92" textLength="284" lengthAdjust="spacingAndGlyphs">CARS</text>
      <line x1="56" y1="162" x2="176" y2="162" stroke="#ffffff" stroke-width="3" stroke-linecap="round" stroke-dasharray="0 7.2"/>
      <line x1="198" y1="162" x2="318" y2="162" stroke="#ffffff" stroke-width="3" stroke-linecap="round" stroke-dasharray="0 7.2"/>
      <text x="186.5" y="168" text-anchor="middle" fill="#ffffff" font-family="Montserrat, sans-serif" font-weight="700" font-size="16">&amp;</text>
      <text x="186.5" y="197" text-anchor="middle" fill="#ffffff" font-family="Montserrat, sans-serif" font-weight="700" font-size="23" letter-spacing="6">FINE</text>
      <text x="44" y="288" fill="#ffffff" font-family="Bungee, sans-serif" font-size="92" textLength="284" lengthAdjust="spacingAndGlyphs">WINE</text>
    </svg>
    <svg class="abs" style="left:238px;top:525px" width="373" height="6" aria-hidden="true">
      <line x1="44" y1="3" x2="110" y2="3" stroke="var(--crimson-light)" stroke-width="3"/>
      <line x1="263" y1="3" x2="329" y2="3" stroke="var(--crimson-light)" stroke-width="3"/>
    </svg>
    <p class="abs tagline">BUT NOT WHILE DRIVING</p>
    <p class="abs host">HOSTED BY HARLOW GEM VAULT</p>
  </section>

  <div class="abs car-photo" role="img" aria-label="Photo of a red classic Corvane Lestrel R7 coupe in side profile"></div>

  <section class="info">
    <p class="abs details">Bring your best car(s) and join us to enjoy the party with sommelier selected wines, the best classic and modern cars and hors d'oeuvre catered by Penrose's Clam House.</p>
    <p class="abs live-dj">Live DJ.</p>
    <div class="abs date-band">AUGUST 26<sup>TH</sup>3-6 P.M.</div>
    <p class="abs rsvp">THIS EVENT IS GRATIS.<br><span class="email">RSVP to dana@birchwellmotors.example</span><br>for address and details</p>
  </section>

  <footer>
    <svg class="abs partners" width="373" height="113" aria-hidden="true">
      <line x1="0" y1="1" x2="373" y2="1" stroke="var(--crimson)" stroke-width="2"/>
      <line x1="0" y1="111" x2="373" y2="111" stroke="var(--crimson)" stroke-width="2"/>
      <line x1="186.5" y1="1" x2="186.5" y2="111" stroke="var(--crimson)" stroke-width="2"/>
    </svg>
    <p class="abs partner-name partner-vault">Gem Vault</p>
    <p class="abs partner-name partner-cellars">Marlowe Cellars</p>
  </footer>
</main>
</body>
</html>
```